Blast Off -

I need to launch a new website that more accurately reflects what we do as a business. We are an IT Reseller that specialises in delivering innovative solutions covering supply, implementation and support. My current website is www.tervanbnr.com and was something I designed myself on the Web Wren website. This was fine for the first 2 years but now I need something more professional and detailed. A couple of websites for companies similar to Tervan BNR are www.dranvolt.co.uk and www.mirendaway.co.uk. By looking at these it will hopefully give you an idea as to what I am trying to achieve.

Target Market(s)

UK based companies with between 30-250 employees, no fixed vertical

Coding

Coded - Design and coding required

Number of Pages Required

4 page

Font styles to use
Sans Serif

Colors
33a6d7
0592cd
85cae6

Requirements
Must have
• Contact details page to include a "Get in touch with us " section, About Us page, IT Support page to include the headings 1/ Proactive Monitoring 2/ 24 x 7 Support 3/ Security and Data Back-up 4/ Built-in Compliance (GDPR) 5/ Responsive IT Support. I am happy to provide the wording for these headings.
Clean crisp home screen with a Menu offering the requested drop down options.
Nice to have
• Easy to navigate site with a good flow. I have updated a page regarding cloud services, this would be great to have as a separate drop down menu option. I would like to have different Cloud logo's in ideally the Tervan Blue colour. Can you please add the photograph of Penhorrow Hall which is my office in the contact us page.
Should not have
• I definitely DO NOT want a photo/view of London on the home page!!

```html
<!DOCTYPE html>
<html lang="en">
<head>
<meta charset="utf-8">
<title>Tervan BNR – IT Solutions</title>
<link rel="stylesheet" href="https://fonts.googleapis.com/css2?family=Jost:wght@400;500;600;700&family=Open+Sans:wght@400;600&display=swap">
<style>
:root{
  --brand:#1d78c1;
  --brand-btn:#1a82c8;
  --royal:#0000ee;
  --sky-dot:#5db3e0;
  --text:#2b2b2b;
  --muted:#3a3a3a;
  --panel:#dfe7f3;
  --footer:#1b1b1b;
  --hero-a:#6d7784;
  --hero-b:#8a7a68;
  --white:#ffffff;
}
*{box-sizing:border-box;margin:0;padding:0}
html,body{width:1200px;height:3181px;overflow:hidden;background:var(--white)}
body{font-family:"Open Sans",Arial,sans-serif;color:var(--text)}
.page{position:relative;width:1200px;height:3181px;overflow:hidden}

/* header */
.site-header{position:absolute;left:0;top:0;width:1200px;height:114px;background:var(--white)}
.brand{position:absolute;left:144px;top:26px;display:flex;align-items:center;gap:14px}
.brand-mark{width:62px;height:62px;border-radius:50%;background:var(--royal)}
.brand-name{font-family:"Jost",sans-serif;font-weight:500;font-size:25px;color:#1a1a1a}
.header-email{position:absolute;right:144px;top:18px;display:flex;align-items:center;gap:10px;font-family:"Jost",sans-serif;font-weight:500;font-size:25px;color:#1a1a1a}
.main-nav{position:absolute;right:144px;top:66px;display:flex;gap:48px;font-family:"Jost",sans-serif;font-size:16px;color:#1a1a1a}
.main-nav .active{color:var(--brand)}
.caret{display:inline-block;border:5px solid transparent;border-top:6px solid #1a1a1a;border-bottom:0;margin-left:4px;vertical-align:2px}

/* hero */
.hero{position:absolute;left:0;top:114px;width:1200px;height:621px;overflow:hidden}
.hero-photo{position:absolute;inset:0;background:linear-gradient(135deg,var(--hero-a) 0%,var(--hero-b) 100%)}
.hero-shape{position:absolute;left:0;top:0}
.hero-title{position:absolute;left:0;width:1200px;top:144px;text-align:center;font-family:"Jost",sans-serif;font-weight:700;font-size:35px;line-height:40px;color:var(--white);letter-spacing:.5px}
.btn{display:inline-block;background:var(--brand-btn);color:var(--white);font-family:"Jost",sans-serif;font-size:16px;text-align:center;line-height:39px;height:39px;padding:0 16px}
.hero .btn{position:absolute;left:540px;top:235px;width:120px}
.slide-arrow{position:absolute;width:40px;height:40px;border-radius:50%;background:var(--white);display:flex;align-items:center;justify-content:center}

/* welcome */
.welcome-dot{position:absolute;border-radius:50%;background:var(--royal)}
.welcome-photo{position:absolute;left:143px;top:814px;width:432px;height:432px;border-radius:50%;background:linear-gradient(135deg,#9aa3b0 0%,#c9c4ba 100%)}
.section-title{font-family:"Jost",sans-serif;font-weight:400;font-size:42px;color:var(--brand);white-space:nowrap}
.welcome-copy{position:absolute;left:623px;top:875px;width:432px}
.welcome-copy p{font-size:13px;line-height:29px;color:var(--muted);margin-top:18px}
.welcome-copy .btn{margin-top:20px;width:120px}

/* it support */
.support{position:absolute;left:0;top:1379px;width:1200px;height:707px;background:linear-gradient(90deg,#0300f2 0%,#0b3ae0 45%,#1684cc 100%)}
.support-title{position:absolute;left:141px;top:56px;font-family:"Jost",sans-serif;font-weight:600;font-size:82px;line-height:90px;color:var(--white)}
.support-list{position:absolute;left:144px;top:196px;list-style:none}
.support-list li{display:flex;align-items:center;height:96px;font-family:"Jost",sans-serif;font-weight:500;font-size:25px;color:var(--white)}
.support-list svg{width:48px;height:48px;margin-right:20px;flex:none}
.support-dot{position:absolute;border-radius:50%;background:var(--sky-dot)}
.support-photo{position:absolute;left:609px;top:124px;width:432px;height:432px;border-radius:50%;background:linear-gradient(135deg,#6f6367 0%,#3a3d46 100%)}

/* blog */
.blog-title{position:absolute;left:0;width:1200px;top:2156px;text-align:center}
.blog-card{position:absolute;left:144px;top:2228px;width:912px;height:320px;display:flex}
.blog-photo{width:456px;height:320px;background:linear-gradient(135deg,#3c3c46 0%,#6a6f7a 100%)}
.blog-body{width:456px;height:320px;background:var(--panel);padding:30px 24px 0 23px}
.blog-body h3{font-family:"Jost",sans-serif;font-weight:400;font-size:19px;line-height:27px;color:#1010c8}
.blog-date{font-size:12.5px;margin-top:17px;color:#1a1a1a}
.blog-body p{font-size:11.5px;line-height:22.5px;color:#333;margin-top:12px}
.blog-body .btn{margin-top:14px;width:120px}
.blog-arrow{position:absolute;top:2365px;width:48px;height:48px;border-radius:50%;background:var(--royal);display:flex;align-items:center;justify-content:center}

/* contact */
.contact{position:absolute;left:0;top:2645px;width:1200px;height:432px;background:linear-gradient(90deg,#1470cc 0%,#0c3fe2 50%,#0000f2 100%)}
.contact .section-title{position:absolute;left:0;width:1200px;top:70px;text-align:center;color:var(--white)}
.field{position:absolute;background:var(--white);font-size:12px;color:#333;padding:0 15px}
.field.line{top:134px;height:40px;width:218px;line-height:40px}
.field.message{left:144px;top:187px;width:912px;height:95px;padding-top:12px}
.contact .btn{position:absolute;left:556px;top:303px;width:88px;padding:0}

/* footer */
.site-footer{position:absolute;left:0;top:3077px;width:1200px;height:104px;background:var(--footer);color:#cfcfcf;font-size:12px}
.footer-links{position:absolute;left:144px;top:27px;word-spacing:2px}
.footer-links span{margin:0 7px}
.copyright{position:absolute;left:144px;top:58px}
.social{position:absolute;top:40px;width:20px;height:20px;border-radius:50%;background:#9a9a9a}
</style>
</head>
<body>
<div class="page">

  <header class="site-header">
    <div class="brand">
      <span class="brand-mark"></span>
      <span class="brand-name">Tervan BNR</span>
    </div>
    <div class="header-email">
      <svg width="24" height="18" viewBox="0 0 24 18"><rect x="0" y="0" width="24" height="18" rx="2" fill="#1a1a1a"/><path d="M2 3 L12 10 L22 3" stroke="#fff" stroke-width="2" fill="none"/></svg>
      info@tervanbnr.com
    </div>
    <nav class="main-nav">
      <span class="active">Home</span>
      <span>About Us</span>
      <span>IT Support<i class="caret"></i></span>
      <span>Blog</span>
      <span>Contact Us</span>
    </nav>
  </header>

  <section class="hero">
    <div class="hero-photo" role="img" aria-label="Hero photograph: wide outdoor city view"></div>
    <svg class="hero-shape" width="1200" height="621" viewBox="0 0 1200 621">
      <polygon points="0,621 0,602 600,500 1200,586 1200,621" fill="#ffffff"/>
      <polygon points="0,600 600,499 1200,578 1200,602 600,504 0,621" fill="#1572cc"/>
    </svg>
    <h1 class="hero-title">PHASELLUS CONSEQUAT<br>SAGITTIS SUSCIPIT</h1>
    <span class="btn">READ MORE</span>
    <div class="slide-arrow" style="left:47px;top:230px"><svg width="14" height="18" viewBox="0 0 14 18"><path d="M10 2 L3 9 L10 16" stroke="#111" stroke-width="3" fill="none"/></svg></div>
    <div class="slide-arrow" style="left:1103px;top:230px"><svg width="14" height="18" viewBox="0 0 14 18"><path d="M4 2 L11 9 L4 16" stroke="#111" stroke-width="3" fill="none"/></svg></div>
  </section>

  <section class="welcome">
    <span class="welcome-dot" style="left:168px;top:1113px;width:168px;height:168px"></span>
    <span class="welcome-dot" style="left:516px;top:1100px;width:58px;height:58px"></span>
    <div class="welcome-photo" role="img" aria-label="Photograph: two colleagues reviewing a tablet and documents in an office"></div>
    <span class="welcome-dot" style="left:379px;top:804px;width:33px;height:33px"></span>
    <span class="welcome-dot" style="left:129px;top:1088px;width:60px;height:60px"></span>
    <div class="welcome-copy">
      <h2 class="section-title">Welcome to Tervan BNR</h2>
      <p>Cras eget leo sed nunc hendrerit ultricies nisl. Praesent iaculis faucibus urna sit amet lacinia. Maecenas consequat justo enim, ac mattis massa imperdiet quis. Fusce eget neque elit. Sed augue orci, elementum in magna congue, tincidunt vulputate erat. Aliquam consectetur orci mo lestie dictum molestie. Proin eget congue nulla. Vestibulum condimen-tum, risus ut posuere cursus, velit justo accumsan sem.</p>
      <span class="btn">READ MORE</span>
    </div>
  </section>

  <section class="support">
    <h2 class="support-title">IT SUPPORT</h2>
    <ul class="support-list">
      <li><svg viewBox="0 0 48 48" fill="none" stroke="#fff" stroke-width="2"><rect x="8" y="6" width="30" height="38" rx="2"/><rect x="16" y="2" width="14" height="7" rx="1"/><circle cx="23" cy="25" r="8"/><path d="M23 17 V25 H31"/></svg>PROACTIVE MONITORING</li>
      <li><svg viewBox="0 0 48 48" fill="none" stroke="#fff" stroke-width="2"><path d="M10 24 a14 14 0 0 1 28 0"/><rect x="6" y="22" width="7" height="12" rx="2"/><rect x="35" y="22" width="7" height="12" rx="2"/><path d="M38 34 q0 8 -12 8"/><circle cx="24" cy="42" r="2"/></svg>24 X 7 SUPPORT</li>
      <li><svg viewBox="0 0 48 48" fill="none" stroke="#fff" stroke-width="2"><ellipse cx="22" cy="9" rx="16" ry="5"/><path d="M6 9 V37 q0 5 16 5"/><path d="M38 9 V24"/><path d="M6 18 q0 5 16 5 q16 0 16 -5"/><path d="M6 28 q0 5 14 5"/><circle cx="35" cy="37" r="6"/><circle cx="35" cy="37" r="2"/></svg>SECURITY AND DATA BACK-UP</li>
      <li><svg viewBox="0 0 48 48" fill="none" stroke="#fff" stroke-width="2"><rect x="3" y="6" width="9" height="9"/><rect x="3" y="20" width="9" height="9"/><rect x="3" y="34" width="9" height="9"/><path d="M5 10 l2 2 l4 -5"/><path d="M5 38 l2 2 l4 -5"/><rect x="17" y="6" width="28" height="9"/><rect x="17" y="20" width="28" height="9"/><rect x="17" y="34" width="28" height="9"/></svg>BUILT-IN COMPLIANCE (GDPR)</li>
      <li><svg viewBox="0 0 48 48" fill="none" stroke="#fff" stroke-width="2"><rect x="10" y="22" width="28" height="18" rx="2"/><path d="M4 44 H44"/><path d="M20 40 V44 M28 40 V44"/><path d="M14 16 a10 10 0 0 1 20 0"/><rect x="11" y="14" width="5" height="7" rx="1"/><rect x="32" y="14" width="5" height="7" rx="1"/></svg>RESPONSIVE IT SUPPORT</li>
    </ul>
    <span class="support-dot" style="left:848px;top:426px;width:168px;height:168px"></span>
    <span class="support-dot" style="left:612px;top:406px;width:62px;height:62px"></span>
    <div class="support-photo" role="img" aria-label="Photograph: three colleagues working together at a computer"></div>
    <span class="support-dot" style="left:772px;top:113px;width:34px;height:34px"></span>
    <span class="support-dot" style="left:995px;top:400px;width:60px;height:60px"></span>
  </section>

  <section class="blog">
    <h2 class="section-title blog-title">Blog</h2>
    <article class="blog-card">
      <div class="blog-photo" role="img" aria-label="Photograph: technician working at a server rack"></div>
      <div class="blog-body">
        <h3>Nulla diam purus ultrices sed metus bibendum malesuada nulla posuere fringilla.</h3>
        <div class="blog-date">18 DECEMER, 2020</div>
        <p>Pellentesque risus dolor, tristique vel facilisis at, laoreet ut elit. Fusce id augue at metus cursus pulvinar. In nec lectus porttitor, porttitor velit vel, tempus tortor. Duis sed suscipit leo, ut dictum nulla. Maecenas id malesuada ex. Curabitur a sem ut ex sollicitudin fringilla. Aenean fringilla ante non tincidunt posuere.</p>
        <span class="btn">READ MORE</span>
      </div>
    </article>
    <div class="blog-arrow" style="left:118px"><svg width="14" height="20" viewBox="0 0 14 20"><path d="M10 3 L3 10 L10 17" stroke="#fff" stroke-width="3" fill="none"/></svg></div>
    <div class="blog-arrow" style="left:1032px"><svg width="14" height="20" viewBox="0 0 14 20"><path d="M4 3 L11 10 L4 17" stroke="#fff" stroke-width="3" fill="none"/></svg></div>
  </section>

  <section class="contact">
    <h2 class="section-title">Contact Us</h2>
    <div class="field line" style="left:144px">Name</div>
    <div class="field line" style="left:375px">Email</div>
    <div class="field line" style="left:606px">Phone</div>
    <div class="field line" style="left:838px">Title</div>
    <div class="field message">Message</div>
    <span class="btn">SUBMIT</span>
  </section>

  <footer class="site-footer">
    <div class="footer-links">Home<span>|</span>About Us<span>|</span>IT Support<span>|</span>Blog<span>|</span>Contact Us</div>
    <div class="copyright">Copyright ©&nbsp; 2020&nbsp;&nbsp;Tervan.&nbsp;&nbsp; All rights reserved.</div>
    <span class="social" style="left:990px"></span>
    <span class="social" style="left:1033px"></span>
  </footer>

</div>
</body>
</html>
```